Facebook Cover & Profile Branding for VelbrooK Systems

We need a modern, premium Facebook cover image for our company Velbrook Systems GmbH. The design should be clean, professional, and aligned with our corporate colors (neon green and deep blue) as well as our logo. It should clearly represent us as a technology and IT consulting company with a strong focus on software testing and quality assurance.

Since Velbrook Systems is also active in the U.S. market, the design may include global or U.S.-related elements (e.g., subtle references to international presence, tech innovation with a global reach).

Requirements:

Integration of the Velbrook logo and brand colors

Modern, premium look with a tech-driven feel

Clear, simple layout that looks good on desktop and mobile

Optional: subtle U.S./international references to highlight our global presence

Goal:
A professional, eye-catching Facebook cover image that strengthens our brand identity and reflects our international expansion into the U.S. market.

Target Market(s)

Medium to large enterprises in the technology, finance, and energy sectors - Companies looking for premium IT consulting, software testing, and quality assurance services - Decision makers and executives (CIOs, CTOs, IT managers) in Europe and the United States - A global audience that values innovation, professionalism, and trust

Industry/Entity Type

Information Technology & Consulting Software Testing & Quality Assurance Technology / Professional Services Global IT Consulting with U.S. Market Presence

Requirements
Must have
• Integration of the Velbrook Systems logo and brand colors (Neon Green & Deep Blue) Modern, premium design with a strong tech-oriented look and feel Clean and professional layout, optimized for both desktop and mobile display Clear visibility of the brand identity (technology, IT consulting, software testing, quality assurance) Subtle reference to U.S. presence / global expansion (to highlight activity in both Germany and the U.S.) Balanced use of colors and space for a high-end, corporate appearance
Nice to have
• Subtle animations or motion effects (e.g., light gradients, moving lines, glowing accents) Dark/Light version option for different moods or seasonal campaigns Integration of social media icons (LinkedIn, Instagram, Facebook) in a clean, minimal way Tech-inspired background elements (digital patterns, abstract shapes, network grids) Space for an optional tagline or slogan (e.g., “Innovation. Quality. Global Impact.”) Adaptability for other platforms (so the design style can be reused for LinkedIn or Twitter headers)
Should not have
• Cluttered or overloaded layouts that reduce clarity Low-quality stock photos or generic imagery that doesn’t fit a premium brand Use of colors outside the Velbrook brand identity (Neon Green & Deep Blue) Outdated design styles (e.g., heavy gradients, 3D effects, drop shadows) Complex text blocks that make the design look busy Elements that distract from the logo and core brand message Pop-art or playful styles that don’t match the premium, professional tech look

```html
<!DOCTYPE html>
<html lang="en">
<head>
<meta charset="utf-8">
<title>Velbrook Systems – Social Media &amp; Facebook Covers</title>
<link rel="stylesheet" href="https://fonts.googleapis.com/css2?family=Roboto:wght@400;500;700&display=swap">
<style>
  :root {
    --navy: #0c2266;
    --navy-deep: #0a1c55;
    --green: #2fe54a;
    --cyan: #1fd3e6;
    --blue: #1c8fe0;
    --white: #ffffff;
    --paper: #ffffff;
    --caption: #222222;
  }
  * { box-sizing: border-box; margin: 0; padding: 0; }
  html, body { width: 1200px; height: 448px; overflow: hidden; background: var(--paper); }
  body { position: relative; font-family: "Roboto", Arial, sans-serif; }
  svg text { font-family: "Roboto", Arial, sans-serif; }
  .board-section { position: absolute; }
  .post-grid { left: 64px; top: 85px; width: 278px; height: 264px; }
  .story-post { left: 520px; top: 73px; width: 170px; height: 302px; }
  .cover { left: 879px; width: 258px; height: 98px; }
  .cover--shapes { top: 119px; }
  .cover--photo { top: 234px; }
  .caption {
    position: absolute; font-size: 6.5px; letter-spacing: 0.2px;
    color: var(--caption); text-transform: uppercase; text-align: center;
  }
  .caption--posts { left: 64px; width: 278px; top: 416px; }
  .caption--covers { left: 879px; width: 258px; top: 340px; }
</style>
</head>
<body>

<svg class="board-section post-grid" viewBox="0 0 594 564" role="group" aria-label="Grid of nine social media posts">
  <defs>
    <linearGradient id="gTealGreen" x1="0" y1="0" x2="1" y2="1">
      <stop offset="0" stop-color="var(--cyan)"/><stop offset="1" stop-color="var(--green)"/>
    </linearGradient>
    <linearGradient id="gGreenCyan" x1="0" y1="1" x2="1" y2="0">
      <stop offset="0" stop-color="var(--green)"/><stop offset="1" stop-color="var(--cyan)"/>
    </linearGradient>
    <linearGradient id="gPhotoLab" x1="0" y1="0" x2="1" y2="1">
      <stop offset="0" stop-color="#2b4f8f"/><stop offset="1" stop-color="#6a8fd0"/>
    </linearGradient>
    <linearGradient id="gPhotoPortrait" x1="0" y1="0" x2="1" y2="1">
      <stop offset="0" stop-color="#1b2f6a"/><stop offset="1" stop-color="#5a6fb0"/>
    </linearGradient>
    <linearGradient id="gPhotoCode" x1="0" y1="0" x2="1" y2="1">
      <stop offset="0" stop-color="#5f7fb8"/><stop offset="1" stop-color="#1d2a4a"/>
    </linearGradient>
  </defs>

  <g class="post post--headline">
    <rect x="0" y="0" width="196" height="196" fill="var(--navy)"/>
    <path d="M0 160 C60 150 150 130 196 40 L196 196 L0 196 Z" fill="url(#gGreenCyan)"/>
    <circle cx="20" cy="27" r="4" fill="var(--green)"/>
    <text x="29" y="30" font-size="9" font-weight="500" fill="var(--white)">Velbrook</text>
    <text font-size="14" font-weight="700" fill="var(--white)">
      <tspan x="31" y="65">LOREM IPSUM</tspan><tspan x="31" y="79">DOLOR SIT AMET,</tspan>
      <tspan x="31" y="93">CONSECTETUR</tspan><tspan x="31" y="107">ADIPISCING ELIT</tspan>
    </text>
  </g>

  <g class="post post--photo">
    <rect x="199" y="0" width="196" height="196" fill="url(#gPhotoPortrait)" role="img" aria-label="Photo: person lit by colourful data light projection"/>
    <circle cx="219" cy="27" r="4" fill="var(--green)"/>
    <text x="228" y="30" font-size="9" font-weight="500" fill="var(--white)">Velbrook</text>
  </g>

  <g class="post post--text">
    <rect x="398" y="0" width="196" height="196" fill="url(#gTealGreen)"/>
    <path d="M520 0 L594 0 L594 120 C570 70 545 30 520 0 Z" fill="var(--navy)"/>
    <text font-size="12.5" fill="var(--navy)">
      <tspan x="428" y="72">Lorem ipsum dolor sit</tspan><tspan x="428" y="85">amet, consectetur</tspan>
      <tspan x="428" y="98">adipiscing elit, sed do</tspan><tspan x="428" y="111">eiusmod tempor</tspan>
      <tspan x="428" y="124">incididunt ut labore et</tspan><tspan x="428" y="137">dolore magna aliqua.</tspan>
    </text>
  </g>

  <g class="post post--headline">
    <rect x="0" y="199" width="196" height="196" fill="url(#gGreenCyan)"/>
    <path d="M0 270 C50 230 150 240 196 300 L196 395 L0 395 Z" fill="var(--navy)"/>
    <text font-size="14" font-weight="700" fill="var(--white)">
      <tspan x="31" y="280">LOREM IPSUM</tspan><tspan x="31" y="295">DOLOR SIT</tspan>
      <tspan x="31" y="310">AMET,</tspan><tspan x="31" y="325">CONSECTETUR</tspan>
      <tspan x="31" y="340">ADIPISCING</tspan><tspan x="31" y="355">ELIT</tspan>
    </text>
    <circle cx="132" cy="375" r="4" fill="var(--green)"/>
    <text x="141" y="378" font-size="9" font-weight="500" fill="var(--white)">Velbrook</text>
  </g>

  <rect class="post post--photo" x="199" y="199" width="196" height="196" fill="url(#gPhotoLab)" role="img" aria-label="Photo: engineers in cleanroom suits working on equipment"/>

  <g class="post post--text">
    <rect x="398" y="199" width="196" height="196" fill="var(--navy)"/>
    <text font-size="12.5" font-weight="500" fill="var(--green)" text-anchor="end">
      <tspan x="554" y="252">Lorem ipsum</tspan><tspan x="554" y="265">dolor sit amet,</tspan>
      <tspan x="554" y="278">consectetur</tspan><tspan x="554" y="291">adipiscing elit,</tspan>
      <tspan x="554" y="304">sed do eiusmod</tspan><tspan x="554" y="317">tempor</tspan>
      <tspan x="554" y="330">incididunt ut</tspan><tspan x="554" y="343">labore et dolore</tspan>
      <tspan x="554" y="356">magna aliqua.</tspan>
    </text>
  </g>

  <g class="post post--headline">
    <rect x="0" y="398" width="196" height="166" fill="url(#gTealGreen)"/>
    <path d="M0 398 L196 398 L196 410 C140 450 70 460 0 455 Z" fill="var(--navy)"/>
    <circle cx="20" cy="424" r="4" fill="var(--green)"/>
    <text x="29" y="427" font-size="9" font-weight="500" fill="var(--white)">Velbrook</text>
    <text font-size="14" font-weight="700" fill="var(--navy)">
      <tspan x="31" y="492">LOREM IPSUM</tspan><tspan x="31" y="506">DOLOR SIT AMET,</tspan>
      <tspan x="31" y="520">CONSECTETUR</tspan><tspan x="31" y="534">ADIPISCING ELIT</tspan>
    </text>
  </g>

  <rect class="post post--photo" x="199" y="398" width="196" height="166" fill="url(#gPhotoCode)" role="img" aria-label="Photo: blurred screen with source code"/>

  <g class="post post--text">
    <rect x="398" y="398" width="196" height="166" fill="url(#gGreenCyan)"/>
    <path d="M563 413 L582 424 L563 435 Z" fill="var(--white)"/>
    <text font-size="12.5" fill="var(--navy)" text-anchor="middle">
      <tspan x="500" y="470">Lorem ipsum dolor sit</tspan><tspan x="500" y="483">amet, consectetur</tspan>
      <tspan x="500" y="496">adipiscing elit, sed do</tspan><tspan x="500" y="509">eiusmod tempor</tspan>
      <tspan x="500" y="522">incididunt ut labore et</tspan><tspan x="500" y="535">dolore magna aliqua.</tspan>
    </text>
  </g>
</svg>
<p class="caption caption--posts">Social media posts</p>

<svg class="board-section story-post" viewBox="0 0 360 640" role="group" aria-label="Story post">
  <defs>
    <linearGradient id="gStory" x1="0" y1="0" x2="0" y2="1">
      <stop offset="0" stop-color="var(--green)"/><stop offset="1" stop-color="var(--cyan)"/>
    </linearGradient>
    <linearGradient id="gStoryPhoto" x1="0" y1="0" x2="1" y2="1">
      <stop offset="0" stop-color="#3a5fa8"/><stop offset="1" stop-color="#7f9fdc"/>
    </linearGradient>
  </defs>
  <rect width="360" height="640" fill="url(#gStory)"/>
  <path d="M0 0 L150 0 C230 60 230 250 120 300 C80 318 40 320 0 318 Z" fill="url(#gStoryPhoto)" role="img" aria-label="Photo: engineers in cleanroom suits"/>
  <text font-size="15" fill="var(--navy)" text-anchor="end">
    <tspan x="330" y="250">Lorem ipsum dolor sit amet,</tspan><tspan x="330" y="268">consectetur adipiscing elit,</tspan>
    <tspan x="330" y="286">sed do eiusmod tempor</tspan><tspan x="330" y="304">incididunt ut labore et</tspan>
    <tspan x="330" y="322">dolore magna aliqua.</tspan>
  </text>
  <path d="M0 420 C60 360 200 350 360 380 L360 640 L0 640 Z" fill="var(--navy)"/>
  <text font-size="22" fill="var(--white)">
    <tspan x="34" y="450">Lorem ipsum dolor sit</tspan><tspan x="34" y="476">amet, consectetur</tspan>
    <tspan x="34" y="502">adipiscing elit, sed do</tspan><tspan x="34" y="528">eiusmod tempor</tspan>
    <tspan x="34" y="554">incididunt ut labore et</tspan><tspan x="34" y="580">dolore magna aliqua.</tspan>
  </text>
  <circle cx="238" cy="612" r="6" fill="var(--green)"/>
  <text x="250" y="617" font-size="15" font-weight="500" fill="var(--white)">Velbrook</text>
</svg>

<svg class="board-section cover cover--shapes" viewBox="0 0 549 209" role="group" aria-label="Facebook cover with brand gradient">
  <defs>
    <linearGradient id="gCoverSoft" x1="0" y1="0" x2="1" y2="0">
      <stop offset="0" stop-color="var(--navy)"/>
      <stop offset=".45" stop-color="var(--navy)"/>
      <stop offset=".75" stop-color="var(--cyan)"/>
      <stop offset="1" stop-color="var(--blue)"/>
    </linearGradient>
  </defs>
  <rect width="549" height="209" fill="url(#gCoverSoft)" role="img" aria-label="Abstract decorative brand shapes in green, cyan and blue"/>
  <rect x="0" y="201" width="549" height="8" fill="var(--green)"/>
  <circle cx="38" cy="43" r="7" fill="var(--green)"/>
  <text x="52" y="48" font-size="16" font-weight="500" fill="var(--white)">Velbrook</text>
  <text x="52" y="58" font-size="7" fill="var(--white)">Velbrook Systems GmbH</text>
  <text font-size="17" font-weight="700" fill="var(--white)">
    <tspan x="21" y="111">EMPOWERING TECHNOLOGY</tspan><tspan x="21" y="133">ENABLING SUCCESS</tspan>
  </text>
</svg>

<svg class="board-section cover cover--photo" viewBox="0 0 549 209" role="group" aria-label="Facebook cover with photo">
  <defs>
    <linearGradient id="gCoverPhoto" x1="0" y1="0" x2="1" y2="1">
      <stop offset="0" stop-color="#2c4e90"/><stop offset="1" stop-color="#8aa6dc"/>
    </linearGradient>
    <linearGradient id="gCoverArc" x1="0" y1="0" x2="1" y2="0">
      <stop offset="0" stop-color="var(--green)"/><stop offset="1" stop-color="var(--cyan)"/>
    </linearGradient>
  </defs>
  <rect width="549" height="209" fill="url(#gCoverPhoto)" role="img" aria-label="Photo: engineers in cleanroom suits inspecting machinery"/>
  <path d="M0 0 L400 0 C330 30 260 40 200 70 C120 95 60 95 0 100 Z" fill="var(--navy)"/>
  <path d="M120 209 C180 150 300 130 420 160 C440 170 455 190 460 209 Z" fill="url(#gCoverArc)"/>
  <circle cx="38" cy="35" r="7" fill="var(--green)"/>
  <text x="52" y="40" font-size="16" font-weight="500" fill="var(--white)">Velbrook</text>
  <text x="52" y="50" font-size="7" fill="var(--white)">Velbrook Systems GmbH</text>
  <text x="21" y="114" font-size="11.5" font-weight="700" fill="var(--white)">EMPOWERING TECHNOLOGY. ENABLING SUCCESS</text>
</svg>
<p class="caption caption--covers">Facebook covers</p>

</body>
</html>
```